Attract renters to our neighborhoods - inform renters who we are

Apartments in several neighborhoods. We want to attract renters who want to live along the lake or other near by neighborhoods. We want them to know that we have an apartment for them in their location.
The perfect location to spend your time.
When minutes matter LIVE where you work and play! (love this tag line)
Updates

www.kvtresidences.example Choose from over 3,700 apartments in Chicago’s most celebrated neighborhoods. 773-582-6041 Chicago’s most celebrated neighborhoods. 31 PROPERTIES

Target Market(s)

Sophisticated apartment renter who wants location, space, amenities

Industry/Entity Type

Apartment Rentals

Requirements
Must have
• Feel like I want to live there, or the ad is calling me
Nice to have
• Appeal to a sophisticated apartment renter. We have what you want, where you want to be.
Should not have
• Logo colors are black and red/burnt orange see attached logo

```html
<!DOCTYPE html>
<html lang="en">
<head>
<meta charset="utf-8">
<title>KVT Residences – The Perfect Location</title>
<link rel="stylesheet" href="https://fonts.googleapis.com/css2?family=Poppins:wght@300;400;500;600;700;800&display=swap">
<style>
  :root{
    --red:#d7262b;
    --red-deep:#a9141a;
    --ink:#111111;
    --white:#ffffff;
    --lake:#2fc1c9;
    --lake-deep:#1aa6b3;
    --sky:#dff1fa;
    --park:#5f8f4a;
    --city:#b9b4ab;
  }
  *{box-sizing:border-box;margin:0;padding:0}
  html,body{width:848px;height:1200px;overflow:hidden;background:var(--white)}
  body{font-family:"Poppins",sans-serif;color:var(--ink)}
  .flyer{position:relative;width:848px;height:1200px;overflow:hidden;background:var(--white)}

  .brand{position:absolute;top:22px;left:0;width:100%;text-align:center;font-weight:800;font-size:62px;line-height:1;letter-spacing:1px;color:var(--ink)}

  .headline{position:absolute;top:104px;left:0;width:100%;text-align:center;font-weight:800;font-size:50px;line-height:1;letter-spacing:-1px;color:var(--ink)}
  .headline .accent{color:var(--red)}
  .subline{position:absolute;top:164px;left:0;width:100%;text-align:center;font-weight:700;font-size:42px;line-height:1;letter-spacing:-0.5px;color:var(--red)}

  .hero{position:absolute;top:210px;left:0;width:848px;height:426px;
    background:linear-gradient(180deg,var(--white) 0%,var(--sky) 12%,var(--city) 22%,var(--park) 42%,#e9dfc6 58%,var(--lake) 70%,var(--lake-deep) 100%)}
  .hero-band{position:absolute;top:635px;left:0;width:848px;height:32px;background:linear-gradient(90deg,var(--red-deep),var(--red))}

  .tagline{position:absolute;left:26px;top:756px;width:290px}
  .tagline .when{position:absolute;left:2px;top:4px;width:96px;height:24px;transform-origin:0 0;transform:translate(0,96px) rotate(-90deg);font-weight:700;font-size:22px;line-height:24px;letter-spacing:1px;text-align:center}
  .tagline .big{position:absolute;left:40px;font-weight:800;font-size:46px;line-height:1;letter-spacing:-0.5px}
  .tagline .minutes{top:0}
  .tagline .matter{top:57px}
  .tagline .live{position:absolute;left:2px;top:108px;font-weight:300;font-size:40px;line-height:1;letter-spacing:-0.5px}
  .tagline .work-box{position:absolute;left:-2px;top:158px;width:280px;height:100px;border:3px solid var(--red);background:linear-gradient(180deg,var(--red) 0 44%,var(--white) 44% 100%)}
  .tagline .work-box span{position:absolute;left:4px;font-weight:800;font-size:42px;line-height:1;letter-spacing:-1px}
  .tagline .work{top:2px;color:var(--white)}
  .tagline .play{top:50px;color:var(--ink)}

  .neighborhoods{position:absolute;left:326px;top:569px;width:487px;height:530px;background:var(--white);box-shadow:0 4px 14px rgba(0,0,0,.25)}
  .banner{position:absolute;left:0;top:0;width:487px;height:90px}
  .banner-text{position:absolute;left:91px;top:16px;color:var(--white);font-size:13px;line-height:24px;font-weight:400;white-space:nowrap}
  .banner-text strong{font-size:17px;font-weight:700}
  .banner-icon{position:absolute;left:38px;top:20px}

  .area{position:absolute;width:220px}
  .area .photo{width:220px;height:164px;border:2px solid var(--red)}
  .area .name{margin:10px 0 0 10px;font-weight:700;font-size:13px;line-height:1}
  .area .rule{margin:5px 0 0 10px;width:52px;height:3px;background:var(--red)}
  .a1{left:12px;top:91px}
  .a2{left:249px;top:91px}
  .a3{left:12px;top:308px}
  .a4{left:249px;top:308px}
  .a1 .photo{background:linear-gradient(180deg,#6cc6ec 0%,#9aa3a8 35%,#7b7f82 70%,var(--lake) 100%)}
  .a2 .photo{background:linear-gradient(180deg,#cfe6f3 0%,#6cb8dc 30%,#8f8a86 60%,#6d6a66 100%)}
  .a3 .photo{background:linear-gradient(180deg,#cfeaf6 0%,#86a37e 30%,#e8dcc0 55%,var(--lake) 75%,var(--lake-deep) 100%)}
  .a4 .photo{background:linear-gradient(180deg,#d7ecf6 0%,#a69d92 30%,#6f9857 55%,var(--lake) 80%,var(--lake-deep) 100%)}
  .card-base{position:absolute;left:324px;top:1097px;width:494px;height:13px;background:linear-gradient(90deg,var(--red-deep),var(--red))}

  .call-tab{position:absolute;left:0;top:1106px;width:300px;height:36px}
  .call-tab span{position:absolute;left:57px;top:3px;color:var(--white);font-weight:700;font-size:22px;line-height:30px}
  .call-line{position:absolute;left:0;top:1137px;width:848px;height:5px;background:var(--ink)}
  .contact-bar{position:absolute;left:0;top:1141px;width:848px;height:59px;background:var(--red);color:var(--white);display:flex;align-items:center;padding-left:20px;white-space:nowrap}
  .contact-bar .phone{font-weight:700;font-size:40px;letter-spacing:-1px;margin-left:8px}
  .contact-bar .divider{width:2px;height:26px;background:var(--white);margin:0 18px}
  .contact-bar .web{font-weight:700;font-size:24px;margin-left:10px;text-transform:uppercase}
</style>
</head>
<body>
<main class="flyer">
  <div class="brand">KVT</div>

  <h1 class="headline">THE PERFECT LOCATI<span class="accent">O</span>N</h1>
  <p class="subline">TO SPEND YOUR TIME</p>

  <div class="hero" role="img" aria-label="Aerial view of the lakefront skyline, park and sandy beach along turquoise lake water"></div>
  <div class="hero-band"></div>

  <section class="tagline">
    <span class="when">WHEN</span>
    <span class="big minutes">MINUTES</span>
    <span class="big matter">MATTER!</span>
    <span class="live">LIVE WHERE</span>
    <div class="work-box">
      <span class="work">YOU WORK</span>
      <span class="play">AND PLAY!</span>
    </div>
  </section>

  <section class="neighborhoods">
    <svg class="banner" viewBox="0 0 487 90" aria-hidden="true">
      <defs>
        <linearGradient id="bannerRed" x1="0" x2="1">
          <stop offset="0" stop-color="#a9141a"/>
          <stop offset="0.5" stop-color="#d7262b"/>
          <stop offset="1" stop-color="#a9141a"/>
        </linearGradient>
      </defs>
      <polygon points="0,0 487,0 444,84 36,84" fill="url(#bannerRed)"/>
    </svg>
    <svg class="banner-icon" width="44" height="44" viewBox="0 0 44 44" aria-hidden="true">
      <g fill="#fff">
        <rect x="12" y="2" width="20" height="40"/>
        <rect x="0" y="18" width="10" height="24"/>
        <rect x="34" y="18" width="10" height="24"/>
      </g>
      <g fill="#c41e24">
        <rect x="15" y="6" width="4" height="4"/><rect x="25" y="6" width="4" height="4"/>
        <rect x="15" y="14" width="4" height="4"/><rect x="25" y="14" width="4" height="4"/>
        <rect x="15" y="22" width="4" height="4"/><rect x="25" y="22" width="4" height="4"/>
        <rect x="19" y="32" width="6" height="10"/>
        <rect x="3" y="24" width="4" height="4"/><rect x="3" y="32" width="4" height="4"/>
        <rect x="37" y="24" width="4" height="4"/><rect x="37" y="32" width="4" height="4"/>
      </g>
    </svg>
    <p class="banner-text">CHOOSE FROM OVER <strong>3,700 APARTMENTS</strong><br>IN CHICAGO’S MOST CELEBRATED NEIGHBORHOODS</p>

    <div class="area a1">
      <div class="photo" role="img" aria-label="Aerial view of Gold Coast high-rises beside the lakeshore"></div>
      <p class="name">GOLD-COAST &amp; OLD TOWN</p><div class="rule"></div>
    </div>
    <div class="area a2">
      <div class="photo" role="img" aria-label="Aerial view of River North towers with the lake behind"></div>
      <p class="name">RIVER NORTH</p><div class="rule"></div>
    </div>
    <div class="area a3">
      <div class="photo" role="img" aria-label="Aerial view of Lincoln Park beach and lakefront parkland"></div>
      <p class="name">LINCOLN PARK</p><div class="rule"></div>
    </div>
    <div class="area a4">
      <div class="photo" role="img" aria-label="Aerial view of Lake View harbor with boats and green park"></div>
      <p class="name">LAKE VIEW</p><div class="rule"></div>
    </div>
  </section>
  <div class="card-base"></div>

  <div class="call-tab">
    <svg width="300" height="36" viewBox="0 0 300 36" aria-hidden="true" style="position:absolute;left:0;top:0">
      <polygon points="0,0 262,0 296,36 0,36" fill="#111"/>
    </svg>
    <span>CALL TODAY</span>
  </div>
  <div class="call-line"></div>

  <footer class="contact-bar">
    <svg width="26" height="26" viewBox="0 0 24 24" aria-hidden="true">
      <path fill="#fff" d="M6.6 10.8a15.1 15.1 0 0 0 6.6 6.6l2.2-2.2c.3-.3.7-.4 1-.2 1.1.4 2.3.6 3.6.6.6 0 1 .4 1 1V20c0 .6-.4 1-1 1A17 17 0 0 1 3 4c0-.6.4-1 1-1h3.5c.6 0 1 .4 1 1 0 1.3.2 2.5.6 3.6.1.3 0 .7-.2 1z"/>
    </svg>
    <span class="phone">773-582-6041</span>
    <span class="divider"></span>
    <svg width="20" height="20" viewBox="0 0 24 24" aria-hidden="true">
      <g fill="none" stroke="#fff" stroke-width="2">
        <circle cx="12" cy="12" r="10"/>
        <ellipse cx="12" cy="12" rx="4.5" ry="10"/>
        <line x1="2" y1="12" x2="22" y2="12"/>
      </g>
    </svg>
    <span class="web">www.kvtresidences.example</span>
  </footer>
</main>
</body>
</html>
```